Fire Hydrant Repair Parts Flyer

We need a flyer advertising both fire hydrant parts and the manufacturers that we are stocking. Our company is Coastal Flowline Supply and we are a parts distributor who sells directly to contractors. I have attached an example flyer that advertises some other parts we stock. We don't want it to look exactly like the old flyer, but we would like it to be structured similarly. I have also attached a background image for the flyer as well as some pictures of the parts we are stocking. I have also attached pictures of the manufacturer logos that we are stocking. We are trying to convey the parts that we are stocking which are: "Traffic Repair Kits", "Main Valve Repair Kits", "Extension Kits", "Replacement Caps & Gaskets", "Replacement Nozzles", Adjustable Hydrant Wrenches", "Hydrant Diffusers", & "Hydrant Oil". I have attached pictures of some of these items that we would like placed on the flyer. Let me know if you have any questions at all.

```html
<!DOCTYPE html>
<html lang="en">
<head>
<meta charset="utf-8">
<title>Coastal Flowline Supply – Fire Pump Repair Parts Flyer</title>
<link href="https://fonts.googleapis.com/css2?family=Montserrat:wght@400;500;700;800;900&display=swap" rel="stylesheet">
<style>
  :root {
    --brand-red: #e8194a;
    --brand-blue: #3a4fa8;
    --panel-blue: #2f4fb8;
    --paper: #ffffff;
    --paper-tint: #f4f6fa;
    --badge-grey: #eceef2;
    --rule-grey: #d3d7e3;
    --hydrant-red: #e5262c;
    --hydrant-dark: #b5151b;
    --parts-grey: #dfe2e8;
    --white: #ffffff;
  }
  * { box-sizing: border-box; margin: 0; padding: 0; }
  html, body {
    width: 700px; height: 1200px; overflow: hidden;
    background: var(--paper);
    font-family: 'Montserrat', Arial, sans-serif;
  }
  .flyer {
    position: relative; width: 700px; height: 1200px; overflow: hidden;
    background: linear-gradient(180deg, var(--paper) 0%, var(--paper-tint) 100%);
  }
  .backdrop { position: absolute; inset: 0; }

  .brand {
    position: absolute; left: 22px; top: 60px;
    display: flex; align-items: center; gap: 12px;
  }
  .brand-dot { width: 34px; height: 34px; border-radius: 50%; background: var(--brand-red); }
  .brand-name { color: var(--brand-blue); font-weight: 500; font-size: 25px; letter-spacing: -0.3px; }

  .headline {
    position: absolute; left: 28px; top: 148px;
    color: var(--brand-red); font-weight: 900; font-size: 84px;
    line-height: 87px; letter-spacing: -2px;
  }
  .subhead {
    position: absolute; left: 31px; top: 420px;
    color: var(--brand-blue); font-weight: 900; font-size: 40px;
    line-height: 52px; letter-spacing: -0.5px;
  }
  .divider {
    position: absolute; left: 30px; top: 550px; width: 310px; height: 2px;
    background: var(--rule-grey);
  }

  .parts-list { position: absolute; top: 595px; list-style: none; }
  .parts-list.col-left { left: 30px; }
  .parts-list.col-right { left: 203px; }
  .parts-list li {
    position: relative; padding-left: 22px;
    color: var(--brand-red); font-weight: 700; font-size: 17px; line-height: 21px;
  }
  .parts-list li::before {
    content: ""; position: absolute; left: 0; top: 4px;
    width: 12px; height: 12px; border-radius: 50%;
    border: 3px solid var(--brand-blue); background: var(--white);
  }
  .col-left li { height: 64px; }
  .col-right li:nth-child(1) { height: 66px; }
  .col-right li:nth-child(2) { height: 62px; }
  .col-right li:nth-child(3) { height: 87px; }

  .maker-panel {
    position: absolute; left: 20px; top: 877px; width: 355px; height: 133px;
    background: var(--badge-grey); border-radius: 12px;
    display: grid; grid-template-columns: repeat(3, 1fr); grid-template-rows: repeat(2, 1fr);
  }
  .maker-badge { display: flex; align-items: center; justify-content: center; }
  .maker-badge:nth-child(3n+2), .maker-badge:nth-child(3n+3) { border-left: 1px solid var(--rule-grey); }
  .maker-badge:nth-child(-n+3) { border-bottom: 1px solid var(--rule-grey); }
  .maker-shape { width: 64px; height: 26px; border-radius: 4px; background: #c9cdd6; }
  .maker-shape.round { width: 34px; height: 34px; border-radius: 50%; }

  .hydrant-photo {
    position: absolute; left: 456px; top: 72px; width: 200px; height: 578px;
    border-radius: 90px 90px 30px 30px;
    background: radial-gradient(ellipse at 40% 30%, var(--hydrant-red) 0%, var(--hydrant-dark) 100%);
  }
  .parts-photo {
    position: absolute; left: 412px; top: 690px; width: 266px; height: 345px;
    border-radius: 16px;
    background: radial-gradient(ellipse at 50% 50%, var(--parts-grey) 0%, rgba(223,226,232,0) 75%);
  }

  .contact {
    position: absolute; left: 0; right: 0; bottom: 0; height: 100px;
    color: var(--white);
  }
  .contact-item { position: absolute; display: flex; align-items: center; gap: 10px; }
  .contact-icon { width: 22px; height: 22px; flex: none; }
  .phone { left: 30px; top: 0; font-weight: 800; font-size: 30px; }
  .web { left: 30px; top: 50px; font-weight: 500; font-size: 19px; }
  .address { left: 376px; top: 2px; font-weight: 500; font-size: 14px; line-height: 18px; }
  .email { left: 376px; top: 52px; font-weight: 500; font-size: 14px; }
</style>
</head>
<body>
<main class="flyer">
  <svg class="backdrop" width="700" height="1200" viewBox="0 0 700 1200" aria-hidden="true">
    <path class="panel" d="M451 0 H700 V471 H424 Q400 471 403 447 Z" fill="var(--panel-blue)"/>
    <line class="panel-accent" x1="447" y1="2" x2="400" y2="343" stroke="var(--brand-red)" stroke-width="3"/>
    <line class="panel-accent" x1="605" y1="488" x2="700" y2="488" stroke="var(--brand-red)" stroke-width="2"/>
    <path class="footer-stripe" d="M0 1058 Q350 1040 700 1050 V1090 H0 Z" fill="var(--brand-red)"/>
    <path class="footer-band" d="M0 1065 Q350 1052 700 1078 V1200 H0 Z" fill="var(--brand-blue)"/>
  </svg>

  <header class="brand">
    <span class="brand-dot"></span>
    <span class="brand-name">Coastal Flowline Supply</span>
  </header>

  <div class="hydrant-photo" role="img" aria-label="Photo of a red fire hydrant with chained caps"></div>

  <h1 class="headline">FIRE<br>PUMP<br>REPAIR</h1>
  <h2 class="subhead">PARTS AND<br>ACCESSORIES</h2>
  <div class="divider"></div>

  <ul class="parts-list col-left">
    <li>TRAFFIC<br>REPAIR KITS</li>
    <li>MAIN VALVE<br>REPAIR KITS</li>
    <li>EXTENSION<br>KITS</li>
    <li>HYDRANT<br>DIFFUSERS</li>
  </ul>
  <ul class="parts-list col-right">
    <li>REPLACEMENT<br>CAPS &amp; GASKETS</li>
    <li>REPLACEMENT<br>NOZZLES</li>
    <li>ADJUSTABLE<br>HYDRANT<br>WRENCHES</li>
    <li>HYDRANT OIL</li>
  </ul>

  <div class="parts-photo" role="img" aria-label="Photos of hydrant parts: repair kit with gaskets and bolts, hydrant wrench, bottle of hydrant oil, diffuser with pressure gauge, replacement cap with chain, extension kit"></div>

  <section class="maker-panel" aria-label="Stocked manufacturers">
    <div class="maker-badge"><span class="maker-shape"></span></div>
    <div class="maker-badge"><span class="maker-shape"></span></div>
    <div class="maker-badge"><span class="maker-shape round"></span></div>
    <div class="maker-badge"><span class="maker-shape"></span></div>
    <div class="maker-badge"><span class="maker-shape"></span></div>
    <div class="maker-badge"><span class="maker-shape"></span></div>
  </section>

  <footer class="contact">
    <div class="contact-item phone">
      <svg class="contact-icon" viewBox="0 0 24 24"><circle cx="12" cy="12" r="12" fill="var(--brand-red)"/><path d="M8.5 6.5l2 2-1.2 1.6a7 7 0 0 0 4.6 4.6l1.6-1.2 2 2-1.4 1.9c-4.6-.4-9-4.8-9.4-9.4z" fill="var(--white)"/></svg>
      <span>(800) 555-0142</span>
    </div>
    <div class="contact-item web">
      <svg class="contact-icon" viewBox="0 0 24 24"><circle cx="12" cy="12" r="12" fill="var(--brand-red)"/><circle cx="12" cy="12" r="6.5" fill="none" stroke="var(--white)" stroke-width="1.5"/><ellipse cx="12" cy="12" rx="2.8" ry="6.5" fill="none" stroke="var(--white)" stroke-width="1.3"/><line x1="5.5" y1="12" x2="18.5" y2="12" stroke="var(--white)" stroke-width="1.3"/></svg>
      <span>www.coastalflowline.com</span>
    </div>
    <div class="contact-item address">
      <svg class="contact-icon" viewBox="0 0 24 24"><circle cx="12" cy="12" r="12" fill="var(--white)"/><path d="M12 5a4.5 4.5 0 0 1 4.5 4.5c0 3.3-4.5 8.5-4.5 8.5S7.5 12.8 7.5 9.5A4.5 4.5 0 0 1 12 5z" fill="var(--brand-red)"/><circle cx="12" cy="9.5" r="1.7" fill="var(--white)"/></svg>
      <span>412 Harbor Point Road<br>Pensacola FL 32502</span>
    </div>
    <div class="contact-item email">
      <svg class="contact-icon" viewBox="0 0 24 24"><circle cx="12" cy="12" r="12" fill="var(--white)"/><rect x="6" y="8" width="12" height="9" rx="1" fill="var(--brand-red)"/><path d="M6.5 8.5l5.5 4.5 5.5-4.5" fill="none" stroke="var(--white)" stroke-width="1.3"/></svg>
      <span>sales@coastalflowline.com</span>
    </div>
  </footer>
</main>
</body>
</html>
```